Estate Planner needs an Ad for a local newsletter

I need an ad designed for my practice as an estate planning attorney. The ad will be in a newsletter that targets individuals over the age of 55. My ad is 7.5"W x 4.6"H (a half page ad) .
The wording should include:
Varnholt, Danielle

Danielle Varnholt

Wisdom Meets Planning
Your Estate, Your Legacy

After 23 years as a military spouse, moving our family of six across the country,
I learned the true value of careful planning. Today I help Palomar County's seniors protect what matters most – their family’s future and their life’s work.

I understand that your estate is more than just assets – it's a lifetime of wise
decisions, cherished memories, and dreams for your family's future.

Professional Estate Planning:
• Wills & Living Trusts • Healthcare Directives
• Power of Attorney • Asset Protection
• Probate Avoidance • Peace of Mind

Plus also needs to have my contact information:
RPV Law
Danielle Varnholt
Attorney/Of Counsel
4712 Cedarbrook Lane
Larkspur Falls, Ohio 45099
(555) 684-1093
dvarnholt@rpvlegalteam.example
Logo is attached.

```html
<!DOCTYPE html>
<html lang="en">
<head>
<meta charset="utf-8">
<title>Danielle Varnholt – Estate Planning Ad</title>
<link rel="stylesheet" href="https://fonts.googleapis.com/css2?family=Tinos:wght@700&family=Montserrat:wght@400;500;600&family=Comfortaa:wght@300;400&display=swap">
<style>
  :root {
    --canvas-bg: #c8cac3;
    --paper: #ffffff;
    --ink: #0d0d0d;
    --brand-blue: #1c5a98;
    --band-blue: #1f5d9c;
    --navy: #142649;
    --light-blue: #4a90d4;
    --rule-blue: #3d7cc0;
    --footer-ink: #1a1a1a;
    --logo-navy: #1b2d55;
  }
  * { margin: 0; padding: 0; box-sizing: border-box; }
  html, body { width: 917px; height: 1200px; overflow: hidden; }
  body { background: var(--canvas-bg); position: relative; font-family: "Montserrat", Arial, sans-serif; }

  .ad {
    position: absolute; left: 30px; top: 340px;
    width: 857px; height: 520px;
    background: var(--paper);
    box-shadow: 0 14px 14px -8px rgba(0,0,0,0.35);
    overflow: hidden;
  }
  .name {
    position: absolute; left: 46px;
    font-family: "Tinos", "Times New Roman", serif; font-weight: 700;
    font-size: 70px; line-height: 1; letter-spacing: 1px;
  }
  .name--first { top: 36px; color: var(--ink); }
  .name--last { top: 104px; color: var(--brand-blue); }

  .navy-panel { position: absolute; left: 0; top: 243px; width: 857px; height: 187px; background: var(--navy); }
  .navy-panel--upper { left: 530px; top: 158px; width: 327px; height: 86px; }

  .tagline-band {
    position: absolute; left: 0; top: 203px; width: 530px; height: 40px;
    background: var(--band-blue); color: #fff;
    font-family: "Comfortaa", "Trebuchet MS", sans-serif; font-weight: 300;
    font-size: 16.5px; line-height: 40px; padding-left: 48px; white-space: nowrap;
  }

  .portrait {
    position: absolute; left: 515px; top: 28px; width: 303px; height: 402px;
    background: linear-gradient(180deg, #c9a58c 0%, #2a2d36 35%, #1a2c4d 65%, #b06a4e 85%, #1f2433 100%);
    border-radius: 90px 90px 0 0;
  }

  .intro {
    position: absolute; left: 46px; top: 253px; width: 470px;
    color: #fff; font-size: 11px; line-height: 17px; font-weight: 400;
  }

  .services-frame {
    position: absolute; left: 34px; top: 303px; width: 433px; height: 111px;
    border-top: 1.5px solid var(--rule-blue); border-left: 1.5px solid var(--rule-blue);
  }
  .services-title {
    position: absolute; left: 46px; top: 311px;
    font-family: "Tinos", "Times New Roman", serif; font-weight: 700;
    font-size: 22px; color: var(--light-blue); white-space: nowrap;
  }
  .services-list {
    position: absolute; top: 346px; list-style: none;
    color: #fff; font-size: 14px; line-height: 20.5px;
  }
  .services-list--left { left: 50px; }
  .services-list--right { left: 281px; }
  .services-list li { position: relative; padding-left: 16px; white-space: nowrap; }
  .services-list li::before {
    content: ""; position: absolute; left: 0; top: 6px;
    width: 8px; height: 9px; background: var(--light-blue);
  }

  .footer { position: absolute; left: 0; top: 430px; width: 857px; height: 90px; }
  .firm-name {
    position: absolute; left: 46px; top: 24px;
    font-family: "Tinos", "Times New Roman", serif; font-weight: 700;
    font-size: 26px; color: var(--logo-navy); letter-spacing: 0.5px;
  }
  .address, .contact {
    position: absolute; top: 28px; text-align: center; font-style: normal;
    color: var(--footer-ink); font-size: 13.5px; line-height: 20px; white-space: nowrap;
  }
  .address { left: 266px; width: 240px; }
  .contact { left: 554px; width: 260px; }
  .contact .phone { font-weight: 600; }
</style>
</head>
<body>
  <section class="ad" aria-label="Estate planning advertisement">
    <h1 class="name name--first">DANIELLE</h1>
    <h1 class="name name--last">VARNHOLT</h1>

    <div class="navy-panel navy-panel--upper"></div>
    <div class="navy-panel"></div>

    <div class="tagline-band">Wisdom Meets Planning&nbsp;&nbsp;Your Estate, Your Legacy</div>

    <div class="portrait" role="img" aria-label="Photo of the attorney smiling, in a dark suit, holding a stack of file folders"></div>

    <p class="intro">I understand that your estate is more than just assets – it's a lifetime of<br>wise decisions, cherished memories, and dreams for your family's future.</p>

    <div class="services-frame"></div>
    <h2 class="services-title">Professional Estate Planning:</h2>
    <ul class="services-list services-list--left">
      <li>Wills &amp; Living Trusts</li>
      <li>Power of Attorney</li>
      <li>Probate Avoidance</li>
    </ul>
    <ul class="services-list services-list--right">
      <li>Healthcare Directives</li>
      <li>Asset Protection</li>
      <li>Peace of Mind</li>
    </ul>

    <footer class="footer">
      <div class="firm-name">RPV Law</div>
      <address class="address">4712 Cedarbrook Lane<br>Larkspur Falls, Ohio 45099</address>
      <div class="contact">
        <div class="phone">(555) 684-1093</div>
        <div class="email">dvarnholt@rpvlegalteam.example</div>
      </div>
    </footer>
  </section>
</body>
</html>
```